Business card design needed

New company based in Brisbane, Australia. Brindle Systems. The business is focused on the delivery of network architecture design and deployment. We will provide both services and the sale of the necessary equipment to deliver the service. Cloud computing is an important element of our focus as this is an emerging market for enterprises in Queensland. Our target marketplace is medium to large corporations with complex infrastructure requirements. IT Management and above will be the typical entry point for us into these accounts. We would like to see the use of various shade of green, design should be clutter free and impress stability, trust and growth.
Updates
Hey Everyone
Just we let you all know we have changed this project to 'committed' payment status.
Looking forward to seeing the designs! Thanks for your efforts.
Best Regards
Marcus
Industry/Entity Type
Architecture
Contact Information for Business Card
Brindle Systems, Marcus Doyle, Sales Director, Level 14 Harlow Tower, 58 Penfold Street, Brisbane QLD 4000, Ph +61 7 3904 2267, M +61 4 4926 1573, E marcus.doyle@brindlesystems-example.com.au
Look and feel
Each slider illustrates characteristics of the customer's brand and the style your logo design should communicate.

```html
<!DOCTYPE html>
<html lang="en">
<head>
<meta charset="utf-8">
<title>Brindle Systems – Business Card</title>
<link href="https://fonts.googleapis.com/css2?family=Arimo:wght@400;700&display=swap" rel="stylesheet">
<style>
  :root {
    --forest: #123d2b;
    --pine: #1e5a3e;
    --leaf: #5fae6e;
    --mint: #bfe3c4;
    --card-light: #f3f8f3;
    --paper: #ffffff;
    --text: #12261c;
    --shadow: rgba(0, 0, 0, 0.45);
  }
  html, body {
    margin: 0;
    padding: 0;
    overflow: hidden;
  }
  body {
    width: 1200px;
    height: 374px;
    background: var(--paper);
    position: relative;
    font-family: "Arimo", Arial, sans-serif;
    color: var(--text);
  }
  .card {
    position: absolute;
    box-shadow: 5px 6px 7px var(--shadow);
    overflow: hidden;
  }

  /* Front */
  .card-front {
    left: 27px;
    top: 30px;
    width: 512px;
    height: 292px;
    background: var(--card-light);
  }
  .front-header {
    position: absolute;
    left: 0;
    top: 0;
    width: 100%;
    height: 108px;
    background: var(--forest);
    border-bottom: 4px solid var(--leaf);
  }
  .brand-square {
    position: absolute;
    left: 62px;
    top: 36px;
    width: 30px;
    height: 30px;
    background: var(--leaf);
  }
  .brand-name {
    position: absolute;
    left: 153px;
    top: 36px;
    margin: 0;
    font-size: 29px;
    font-weight: 700;
    line-height: 1;
    color: var(--paper);
  }
  .person {
    position: absolute;
    left: 13px;
    top: 130px;
  }
  .person-name {
    margin: 0;
    font-size: 20px;
    font-weight: 400;
    line-height: 24px;
    color: var(--forest);
  }
  .person-title {
    margin: 0;
    font-size: 19px;
    line-height: 24px;
    color: var(--pine);
  }
  .divider {
    position: absolute;
    left: 293px;
    top: 140px;
    width: 1px;
    height: 137px;
    background: var(--leaf);
  }
  .contact {
    position: absolute;
    left: 305px;
    top: 141px;
    font-size: 17px;
    line-height: 23.5px;
    font-style: normal;
  }
  .contact p {
    margin: 0;
    white-space: nowrap;
  }
  .contact-line {
    display: flex;
    align-items: center;
  }
  .contact-icon {
    width: 18px;
    height: 18px;
    margin-right: 10px;
    flex: none;
  }

  /* Back */
  .card-back {
    left: 632px;
    top: 32px;
    width: 516px;
    height: 291px;
    background: var(--forest);
    color: var(--paper);
  }
  .back-band {
    position: absolute;
    left: 0;
    bottom: 0;
    width: 100%;
    height: 6px;
    background: var(--leaf);
  }
  .back-brand {
    position: absolute;
    left: 0;
    top: 104px;
    width: 100%;
    margin: 0;
    text-align: center;
    font-size: 34px;
    font-weight: 700;
    line-height: 1;
  }
  .web {
    position: absolute;
    left: 0;
    top: 232px;
    width: 100%;
    margin: 0;
    text-align: center;
    font-size: 19px;
    line-height: 1;
    color: var(--mint);
  }
</style>
</head>
<body>

<section class="card card-front" aria-label="Business card front">
  <header class="front-header">
    <span class="brand-square" aria-hidden="true"></span>
    <h1 class="brand-name">Brindle Systems</h1>
  </header>

  <div class="person">
    <p class="person-name">Marcus Doyle</p>
    <p class="person-title">Sales Director</p>
  </div>

  <span class="divider" aria-hidden="true"></span>

  <address class="contact">
    <p>Level 14 Harlow Tower</p>
    <p>58 Penfold Street</p>
    <p>Brisbane QLD 4000</p>
    <p class="contact-line">
      <svg class="contact-icon" viewBox="0 0 18 18" aria-hidden="true">
        <circle cx="9" cy="9" r="7.6" fill="none" stroke="#1e5a3e" stroke-width="1.4"/>
        <path d="M6.2 4.8 L7.6 4.6 L8.3 6.9 L7.3 7.6 C7.7 8.7 8.5 9.8 9.8 10.6 L10.7 9.7 L12.9 10.6 L12.7 12 C10 12.5 5.6 8.6 6.2 4.8 Z" fill="#1e5a3e"/>
      </svg>
      +61 7 3904 2267
    </p>
    <p class="contact-line">
      <svg class="contact-icon" viewBox="0 0 18 18" aria-hidden="true">
        <rect x="5.5" y="1.5" width="7" height="15" rx="1" fill="none" stroke="#1e5a3e" stroke-width="1.4"/>
        <rect x="7" y="3.5" width="4" height="6" fill="#1e5a3e"/>
      </svg>
      +61 4 4926 1573
    </p>
    <p class="contact-line">
      <svg class="contact-icon" viewBox="0 0 18 18" aria-hidden="true">
        <rect x="1.5" y="4" width="15" height="10" fill="none" stroke="#1e5a3e" stroke-width="1.4"/>
        <path d="M1.5 4 L9 10 L16.5 4" fill="none" stroke="#1e5a3e" stroke-width="1.4"/>
      </svg>
      marcus.doyle
    </p>
  </address>
</section>

<section class="card card-back" aria-label="Business card back">
  <p class="back-brand">Brindle Systems</p>
  <p class="web">@ brindlesystems-example.com.au</p>
  <span class="back-band" aria-hidden="true"></span>
</section>

</body>
</html>
```